Chistmas Season Card Design Project

Design a Season's Greetings Card 2021 for a law firm

Target Market(s)

Clients of companies

Industry/Entity Type

Legal

Colors
0054AA
0677BA
7BADD7
CADEEF
E8F1F8
EB3D1F
EC4F4E
F09395
F8D3D4
FCEDEE

```html
<!DOCTYPE html>
<html lang="es">
<head>
<meta charset="utf-8">
<title>Season's Greetings 2021</title>
<link rel="stylesheet" href="https://fonts.googleapis.com/css2?family=Damion&display=swap">
<style>
  :root {
    --blue-deep: #0a3ff0;
    --blue-band: #2a8de8;
    --blue-light: #85c2f1;
    --ice: #e8f1f8;
    --white: #ffffff;
    --red: #eb3d1f;
    --rose: #ec4f4e;
    --pink: #f09395;
    --pink-soft: #f8d3d4;
    --plum: #4a1a40;
  }
  html, body {
    margin: 0;
    padding: 0;
    width: 1200px;
    height: 830px;
    overflow: hidden;
    background: var(--white);
  }
  .sheet {
    position: relative;
    width: 1200px;
    height: 830px;
  }
  .card {
    position: absolute;
    top: 13px;
    width: 563px;
    height: 797px;
    background: var(--blue-band);
    overflow: hidden;
    font-family: "Damion", cursive;
  }
  .card--es { left: 23px; }
  .card--en { left: 619px; }

  .band-light {
    position: absolute;
    left: 0;
    width: 100%;
    background: var(--blue-light);
  }
  .band-light--top { top: 28px; height: 150px; }
  .band-light--bottom { top: 642px; height: 123px; }

  .corner-star {
    position: absolute;
    top: 16px;
    right: 22px;
    width: 48px;
    height: 48px;
  }

  .card-title {
    position: absolute;
    top: 58px;
    left: 0;
    width: 100%;
    margin: 0;
    text-align: center;
    font-weight: 400;
    font-size: 74px;
    line-height: 1;
    white-space: nowrap;
    color: var(--blue-deep);
    text-shadow: 3px 3px 0 var(--white);
  }

  .year-outline {
    position: absolute;
    left: 27px;
    top: 222px;
    width: 500px;
    height: 336px;
  }

  .greeting {
    position: absolute;
    top: 224px;
    left: 0;
    width: 100%;
    margin: 0;
    text-align: center;
    font-size: 48px;
    line-height: 80px;
    white-space: nowrap;
    color: var(--ice);
    text-shadow: 3px 3px 0 var(--blue-deep);
  }

  .tree-star {
    position: absolute;
    left: 90px;
    top: 548px;
    width: 50px;
    height: 50px;
  }
  .tree-sparkles {
    position: absolute;
    left: 22px;
    top: 604px;
    width: 196px;
    height: 193px;
    border-radius: 50% 50% 20% 20% / 60% 60% 20% 20%;
    background: radial-gradient(ellipse at 50% 55%,
      rgba(235, 61, 31, 0.55) 0%,
      rgba(236, 79, 78, 0.4) 40%,
      rgba(240, 147, 149, 0.2) 70%,
      rgba(240, 147, 149, 0) 100%);
  }

  .firm-name {
    position: absolute;
    left: 240px;
    top: 664px;
    width: 310px;
    text-align: center;
    color: var(--plum);
    font-size: 27px;
    line-height: 27px;
    white-space: nowrap;
  }
  .firm-name span { display: block; }
</style>
</head>
<body>
<main class="sheet">

  <section class="card card--es" lang="es">
    <div class="band-light band-light--top"></div>
    <div class="band-light band-light--bottom"></div>
    <svg class="corner-star" viewBox="0 0 48 48" aria-hidden="true">
      <polygon fill="var(--ice)" points="24,0 27,18 42,6 30,21 48,24 30,27 42,42 27,30 24,48 21,30 6,42 18,27 0,24 18,21 6,6 21,18"/>
    </svg>
    <h1 class="card-title">Feliz Navidad!</h1>
    <svg class="year-outline" viewBox="0 0 500 336" aria-hidden="true">
      <text x="250" y="326" text-anchor="middle" textLength="490" lengthAdjust="spacingAndGlyphs"
            font-family="Arial, sans-serif" font-size="440" fill="none"
            stroke="var(--ice)" stroke-opacity="0.45" stroke-width="1.2">2021</text>
    </svg>
    <p class="greeting">
      Con mis mejores deseos,<br>
      para que esta noche de paz<br>
      sea tan solo el comienzo<br>
      de un año pleno de éxitos.
    </p>
    <svg class="tree-star" viewBox="0 0 48 48" aria-hidden="true">
      <polygon fill="var(--pink-soft)" points="24,0 27,18 42,6 30,21 48,24 30,27 42,42 27,30 24,48 21,30 6,42 18,27 0,24 18,21 6,6 21,18"/>
    </svg>
    <div class="tree-sparkles" role="img" aria-label="Christmas tree formed by scattered red and pink stars"></div>
    <div class="firm-name">
      <span>Moreno Ibarra &amp;</span>
      <span>Castell Vidal</span>
      <span>Abogados</span>
    </div>
  </section>

  <section class="card card--en" lang="en">
    <div class="band-light band-light--top"></div>
    <div class="band-light band-light--bottom"></div>
    <svg class="corner-star" viewBox="0 0 48 48" aria-hidden="true">
      <polygon fill="var(--ice)" points="24,0 27,18 42,6 30,21 48,24 30,27 42,42 27,30 24,48 21,30 6,42 18,27 0,24 18,21 6,6 21,18"/>
    </svg>
    <h1 class="card-title">Merry Christmas!</h1>
    <svg class="year-outline" viewBox="0 0 500 336" aria-hidden="true">
      <text x="250" y="326" text-anchor="middle" textLength="490" lengthAdjust="spacingAndGlyphs"
            font-family="Arial, sans-serif" font-size="440" fill="none"
            stroke="var(--ice)" stroke-opacity="0.45" stroke-width="1.2">2021</text>
    </svg>
    <p class="greeting">
      Best wishes,<br>
      that this silent night<br>
      is just the beginning<br>
      of a successful year.
    </p>
    <svg class="tree-star" viewBox="0 0 48 48" aria-hidden="true">
      <polygon fill="var(--pink-soft)" points="24,0 27,18 42,6 30,21 48,24 30,27 42,42 27,30 24,48 21,30 6,42 18,27 0,24 18,21 6,6 21,18"/>
    </svg>
    <div class="tree-sparkles" role="img" aria-label="Christmas tree formed by scattered red and pink stars"></div>
    <div class="firm-name">
      <span>Moreno Ibarra &amp;</span>
      <span>Castell Vidal</span>
      <span>Abogados</span>
    </div>
  </section>

</main>
</body>
</html>
```